Popcorn Bag design

We need package design for the launch of our popcorn. We have chosen Hawaiian salts - Red and Black Lava - as our salts. Based on that decision we want to take a bit of a aloha spirit on the bag. Not over the top, but clearly a Hawaiian feel.. Required a Big Kahuna, smiling and with one arm out with a hang loose hand. The basic design will be used for multiple flavors of popcorn and a larger and smaller bags.
Please see the attached word document with more information.
Popcorn flavors for the design
Alaea Hawaiian Red Sea Salt
Alaea Hawaiian Red Sea Salt and Black Pepper
Black Hawaiian Lava Salt on Blue Kernels
The winning design will include the following
Design for the overall package - front and back (we have provided some information for the front and back of the bag.
Big Kahuna (smiling, with one arm out showing the "hang loose" hand samples. File(s) attached.
We will upload our logo, nutrition label and other
The winner will provide the following files:
Front and back of design - artwork ready
Front transparent background
Back transparent background
Big Kahuna transparent background

```html
<!DOCTYPE html>
<html lang="en">
<head>
<meta charset="utf-8">
<title>Kona Pop Popcorn – Bag Front</title>
<link rel="stylesheet" href="https://fonts.googleapis.com/css2?family=Lato:ital,wght@0,400;0,700;1,700&family=Kaushan+Script&family=Yesteryear&display=swap">
<style>
  :root{
    --stage:#3a3a3c;
    --stripe-grey:#b5bac3;
    --stripe-white:#f4f4f1;
    --navy:#1e2b48;
    --navy-soft:#34446a;
    --red:#e8262e;
    --white:#ffffff;
    --popcorn-light:#fbf7ea;
    --popcorn-mid:#eadfb8;
  }
  *{box-sizing:border-box;margin:0;padding:0}
  html,body{width:1200px;height:924px;overflow:hidden;background:var(--stage)}
  .bag-front{
    position:absolute;left:296px;top:32px;width:608px;height:860px;overflow:hidden;
    background:repeating-linear-gradient(90deg,var(--stripe-grey) 0 55px,var(--stripe-white) 55px 110px);
    font-family:'Lato',sans-serif;color:var(--navy);
  }
  .title-panel{position:absolute;left:0;top:0;width:608px;height:320px}
  .brand-name{
    position:absolute;left:126px;width:356px;top:62px;text-align:center;
    font-family:'Lato',sans-serif;font-weight:700;font-size:50px;letter-spacing:3px;color:var(--red);
  }
  .product-word{
    position:absolute;left:40px;width:560px;top:118px;text-align:center;
    font-family:'Yesteryear',cursive;font-size:168px;line-height:1;color:var(--navy);
    transform:rotate(-7deg);
  }
  .tagline{
    position:absolute;left:290px;top:278px;width:200px;text-align:center;
    font-family:'Kaushan Script',cursive;font-size:27px;line-height:1.05;color:var(--red);
    transform:rotate(-9deg);
  }
  .flavor-band{
    position:absolute;left:230px;top:369px;width:378px;height:36px;
    background:var(--navy);border-radius:36px 0 0 0;
    color:var(--white);font-style:italic;font-weight:700;font-size:20px;
    display:flex;align-items:center;justify-content:center;
  }
  .rule{position:absolute;left:0;width:608px;height:3px;background:var(--navy)}
  .popcorn-photo{
    position:absolute;left:0;top:408px;width:608px;height:240px;
    background:radial-gradient(ellipse 70% 80% at 60% 70%,var(--popcorn-mid),var(--popcorn-light) 70%,var(--white));
  }
  .benefits{
    position:absolute;left:226px;top:651px;width:382px;height:100px;
    background:var(--navy);border-radius:0 0 0 60px / 0 0 0 60px;
    border-top-left-radius:60px;
    list-style:none;padding:12px 0 0 82px;color:var(--white);font-weight:700;font-size:21px;line-height:27px;
  }
  .benefits li{display:flex;align-items:center;gap:8px}
  .benefits svg{width:20px;height:20px;flex:none}
  .mascot{
    position:absolute;left:22px;top:362px;width:208px;height:320px;
    background:linear-gradient(180deg,var(--navy-soft),var(--navy));
    border-radius:50% 50% 18px 18px / 14% 14% 6% 6%;
  }
  .mascot-seal{
    position:absolute;left:46px;top:640px;width:160px;height:122px;
    background:var(--navy);border-radius:10px 10px 80px 80px;
    color:var(--white);font-size:18px;line-height:24px;text-align:center;padding-top:50px;
  }
  .claims{position:absolute;left:40px;top:768px;width:170px;text-align:center;font-size:18px;line-height:30px}
  .claims li{list-style:none;border-bottom:1px solid #8f96a3}
  .net-weight{
    position:absolute;left:350px;top:773px;width:206px;height:87px;
    background:var(--navy);border-radius:103px 103px 0 0 / 87px 87px 0 0;
    color:var(--white);font-size:18px;line-height:23px;text-align:center;padding-top:20px;
  }
</style>
</head>
<body>
  <main class="bag-front">
    <svg class="title-panel" viewBox="0 0 608 320" aria-hidden="true">
      <polygon points="126,0 482,0 482,243 126,299" fill="#ffffff"/>
      <line x1="129" y1="0" x2="129" y2="140" stroke="#1e2b48" stroke-width="7"/>
      <line x1="479" y1="0" x2="479" y2="243" stroke="#1e2b48" stroke-width="7"/>
      <line x1="90" y1="306" x2="482" y2="243" stroke="#1e2b48" stroke-width="5"/>
    </svg>
    <div class="brand-name">KONA POP</div>
    <h1 class="product-word">Popcorn</h1>
    <p class="tagline">Taste The<br>Difference</p>

    <div class="rule" style="top:403px"></div>
    <div class="flavor-band">Alaea Hawaiian Red Sea Salt</div>
    <div class="popcorn-photo" role="img" aria-label="Photo of a pile of white popped popcorn"></div>
    <div class="rule" style="top:647px"></div>

    <ul class="benefits">
      <li><svg viewBox="0 0 20 20"><circle cx="10" cy="10" r="10" fill="#fff"/><path d="M5 10.5l3.2 3.2L15 7" stroke="#1e2b48" stroke-width="2.6" fill="none"/></svg>Naturally lower in sodium</li>
      <li><svg viewBox="0 0 20 20"><circle cx="10" cy="10" r="10" fill="#fff"/><path d="M5 10.5l3.2 3.2L15 7" stroke="#1e2b48" stroke-width="2.6" fill="none"/></svg>Higher in iron</li>
      <li><svg viewBox="0 0 20 20"><circle cx="10" cy="10" r="10" fill="#fff"/><path d="M5 10.5l3.2 3.2L15 7" stroke="#1e2b48" stroke-width="2.6" fill="none"/></svg>Smooth rich flavor</li>
    </ul>

    <div class="mascot-seal">Big Kahuna<br>Approved</div>
    <div class="mascot" role="img" aria-label="Navy Big Kahuna tiki mascot illustration"></div>

    <ul class="claims">
      <li>Popped with Aloha</li>
      <li>Gluten Free</li>
    </ul>

    <div class="net-weight">Net weight<br>4.4oz</div>
  </main>
</body>
</html>
```